Quellmark Exteriors Needs a New Website!

We are an exteriors company specializing in vinyl siding, Morten Calloway siding, aluminum soffit/fascia, trough. We do new construction work as well as renovations. We also build detached garages.
You can view our current website at www.quellmarkbuilders.ca
I want to completely overhaul the website.
Our services are different now as we no longer do new home construction as well as we do not do the snow clearing.
I want to focus on 2 things in particular on the website:

1/ Exterior renovations

2/ Detached Garage construction.

I have included our logo in the attached files to use as well.

Some features we would like:

1/ Be able to easily attach a video from Youtube/Vimeo to highlight a product or service
2/ Quick chat or contact button that we can talk to a potential client quickly
3/ Meet the Team page that is interesting and fresh
4/ Place for us to put in helpful exterior tips/suggestions for homeowners.

Content is not important, but looking for the best design that will attract people once they click on our page and want to renovate with us.

Target Market(s)

People looking for renovations on their home, people looking to build a detached garage.

Industry/Entity Type

Residential Construction

Coding

Coded - Design and coding required

Number of Pages Required

5+ page

Font styles to use
Sans Serif

Requirements
Must have
• Fresh and exciting home page.

Simple design. Don't want it over complicated or too much information to confuse the potential client.

Easy way to contact us.

Meet the team page that instills confidence
Nice to have
• Colour of website to go off our logo. Doesn't need to be an exact match, but something that goes well with our blue and grey.

```html
<!DOCTYPE html>
<html lang="en">
<head>
<meta charset="utf-8">
<title>Meet the Team – Quellmark Exteriors</title>
<link href="https://fonts.googleapis.com/css2?family=Montserrat:wght@400;500;600;700;800&display=swap" rel="stylesheet">
<style>
:root{
  --blue:#0d6fc0;
  --blue-dark:#0a5fa8;
  --ink:#111418;
  --text:#3b3f45;
  --page:#f4f8fc;
  --panel:#dff0fa;
  --line:#cfd6dd;
  --white:#ffffff;
  --black:#0b0b0b;
}
*{margin:0;padding:0;box-sizing:border-box}
html,body{width:1200px;height:4082px;overflow:hidden}
body{position:relative;background:var(--page);font-family:'Montserrat',sans-serif;color:var(--text)}
.abs{position:absolute}
.hero-photo{position:absolute;left:0;top:0;width:1200px;height:602px;
  background:linear-gradient(180deg,#8f9c82 0%,#a2a179 30%,#7c7548 60%,#3e3a22 100%);
  clip-path:polygon(0 0,1200px 0,1200px 393px,0 602px)}
.hero-shade{position:absolute;left:0;top:0;width:1200px;height:602px;
  background:linear-gradient(180deg,rgba(20,30,40,.35),rgba(0,0,0,0) 35%,rgba(0,0,0,.25));
  clip-path:polygon(0 0,1200px 0,1200px 393px,0 602px)}
.brand{position:absolute;display:flex;align-items:center;gap:10px;color:var(--white);font-weight:700;letter-spacing:.5px}
.brand-dot{border:3px solid var(--white);border-radius:50%}
.nav-top{left:162px;top:20px;font-size:26px}
.nav-top .brand-dot{width:50px;height:50px}
.menu{position:absolute;top:38px;left:0;width:1200px;height:20px;font-size:13px;font-weight:500;color:var(--white)}
.menu span{position:absolute;white-space:nowrap}
.menu .active{color:var(--blue);font-weight:700}
.menu-underline{position:absolute;left:797px;top:88px;width:118px;height:3px;background:var(--blue)}
.nav-rule{position:absolute;left:162px;top:90px;width:876px;height:1px;background:rgba(255,255,255,.35)}
.hero-title{left:162px;top:270px;font-size:43px;font-weight:800;color:var(--white)}
.crumb{left:162px;top:326px;font-size:12px;font-weight:500;color:var(--white)}
.sec-title{left:0;width:1200px;text-align:center;font-size:30px;font-weight:800;color:var(--ink);letter-spacing:.5px}
.sec-title em{font-style:normal;color:var(--blue)}
.sec-bar{left:570px;width:60px;height:3px;background:var(--blue)}
.member{position:absolute;left:162px;width:876px;height:263px}
.member .photo{position:absolute;left:0;top:0;width:187px;height:187px;border-radius:50%;
  background:radial-gradient(circle at 50% 45%,#8fa0b0 0%,#8c8d66 55%,#6d6a3c 100%)}
.member .info{position:absolute;left:225px;top:22px;width:651px}
.member h3{font-size:19px;font-weight:500;color:var(--blue);line-height:24px}
.member h4{font-size:12px;font-weight:600;color:var(--ink);margin-bottom:8px}
.member p{font-size:11.6px;line-height:22.5px;text-align:justify;margin-bottom:8px}
.member p a{color:var(--blue);text-decoration:none}
.member .sep{position:absolute;left:-3px;top:225px;width:880px;border-top:1px dashed var(--line)}
.footer-band{position:absolute;left:0;top:3268px;width:1200px;height:814px;background:var(--blue);
  clip-path:polygon(0 184px,1200px 0,1200px 814px,0 814px)}
.panel-shadow2{left:174px;top:3520px;width:850px;height:38px;background:#8cc2ea;border-radius:6px}
.panel-shadow1{left:166px;top:3515px;width:866px;height:32px;background:#c8e3f6;border-radius:6px}
.panel{left:160px;top:3027px;width:877px;height:504px;background:var(--panel);border-radius:6px}
.field{position:absolute;background:var(--white);border:1px solid #c9d3dc;font-size:10.5px;color:#6b7178;padding:14px 16px}
.captcha{left:466px;top:3371px;width:265px;height:45px;background:#f9f9f9;border:1px solid #d5d5d5;border-radius:3px;font-size:10px;color:#222;display:flex;align-items:center;padding-left:10px;gap:8px}
.captcha i{width:20px;height:20px;border:2px solid #c1c1c1;background:#fff;display:block}
.submit{left:539px;top:3432px;width:122px;height:36px;background:var(--blue);color:var(--white);font-size:12px;font-weight:700;display:flex;align-items:center;justify-content:center;border-radius:2px}
.chat{left:1112px;top:3221px;width:64px;height:64px;border-radius:50%;background:var(--white);box-shadow:0 4px 14px rgba(0,0,0,.15);display:flex;align-items:center;justify-content:center}
.foot-brand{left:0;width:1200px;top:3668px;justify-content:center;font-size:38px}
.foot-brand .brand-dot{width:68px;height:68px;border-width:4px}
.foot-menu{position:absolute;top:3791px;left:0;width:1200px;font-size:14px;font-weight:500;color:var(--white)}
.foot-menu span{position:absolute;white-space:nowrap}
.foot-menu i{position:absolute;top:2px;width:1px;height:14px;background:rgba(255,255,255,.35)}
.contact{position:absolute;top:3862px;width:320px;text-align:center;color:var(--white)}
.contact svg{display:block;margin:0 auto 18px}
.contact b{display:block;font-size:13px;font-weight:700;margin-bottom:6px}
.contact span{font-size:12px;line-height:20px}
.bottom{left:0;top:4031px;width:1200px;height:51px;background:var(--black);color:var(--white);font-size:11.5px}
.bottom p{position:absolute;left:162px;top:18px}
.social{position:absolute;top:12px;width:28px;height:28px;border-radius:50%;background:var(--blue);border:2px solid var(--white)}
</style>
</head>
<body>

<div class="hero-photo" role="img" aria-label="Team photo of nine staff members standing in a tall grass field"></div>
<div class="hero-shade"></div>

<div class="brand nav-top"><span class="brand-dot"></span>QUELLMARK</div>
<nav class="menu">
  <span style="left:497px">HOME</span>
  <span style="left:580px">ABOUT US</span>
  <span style="left:691px">SERVICES</span>
  <span class="active" style="left:798px">MEET THE TEAM</span>
  <span style="left:950px">CONTACT US</span>
</nav>
<div class="nav-rule"></div>
<div class="menu-underline"></div>

<h1 class="abs hero-title">MEET THE TEAM</h1>
<div class="abs crumb">HOME - MEET THE TEAM</div>

<h2 class="abs sec-title" style="top:590px">MEET <em>THE TEAM</em></h2>
<div class="abs sec-bar" style="top:632px"></div>

<div class="member" style="top:658px">
  <div class="photo" role="img" aria-label="Portrait of Darren Whitlock"></div>
  <div class="info">
    <h3>Darren Whitlock</h3><h4>General Manager</h4>
    <p>Darren is the owner and General Manager of Quellmark Builders. He is principally focused on the building component of the company in addition to overseeing all divisions of Quellmark.</p>
    <p>Darren is married with 5 children and is also Associate Pastor at Riverbend Community Church of Sherwood Park <a>(riverbendchurchsp.ca)</a>.</p>
  </div>
  <div class="sep"></div>
</div>

<div class="member" style="top:921px">
  <div class="photo" role="img" aria-label="Portrait of Owen Pryce"></div>
  <div class="info">
    <h3>Owen Pryce</h3><h4>Operations Manager (Exteriors)</h4>
    <p>Owen started with Quellmark as a delivery driver around two and a half years ago. Since then, he has transitioned into management of our growing exteriors division. He also handles the development of our tech systems to advance company efficiency and productivity.</p>
  </div>
  <div class="sep"></div>
</div>

<div class="member" style="top:1184px">
  <div class="photo" role="img" aria-label="Portrait of Lucan Verhoef"></div>
  <div class="info">
    <h3>Lucan Verhoef</h3><h4>Field Service Manager</h4>
    <p>Lucan oversees the contracting division for Quellmark which includes snow clearing for the winter season. He also manages the custom metal bending shop where all of our custom exterior trims are produced.</p>
    <p>Lucan is married with 7 children and is actively involved at Northgate Fellowship Church of Edmonton.</p>
  </div>
  <div class="sep"></div>
</div>

<div class="member" style="top:1447px">
  <div class="photo" role="img" aria-label="Portrait of Tobias Farrow"></div>
  <div class="info">
    <h3>Tobias Farrow</h3><h4>Site Supervisor</h4>
    <p>Tobias is a journeyman carpenter and oversees all of Quellmark's new building sites. He has been working at Quellmark since 2010, shortly after Quellmark Builders Ltd. was founded. As one Quellmark's first employees, Tobias has a proven track record of commitment to quality and craftsmanship.</p>
    <p>Tobias is engaged to be married next spring and will be settling down in the Edmonton area.</p>
  </div>
  <div class="sep"></div>
</div>

<div class="member" style="top:1710px">
  <div class="photo" role="img" aria-label="Portrait of Miles Farrow"></div>
  <div class="info">
    <h3>Miles Farrow</h3><h4>Renovations Manager</h4>
    <p>In addition to heading up our service department, Miles also is active in managing our exterior renovations division.</p>
    <p>Miles is a skilled musician and can often be found ‘tickling the ivories.’ He also enjoys swimming with dolphins off the shore of Costa Rica and doing one-handed push-ups.</p>
  </div>
  <div class="sep"></div>
</div>

<div class="member" style="top:1973px">
  <div class="photo" role="img" aria-label="Portrait of Reid Farrow"></div>
  <div class="info">
    <h3>Reid Farrow</h3><h4>Lead Installer</h4>
    <p>Reid has been part of the Quellmark team for almost 5 years and is now lead installer for our exterior divisions.</p>
    <p>He ensures all projects are completed with the highest standard of quality, in a timely manner, and with the least possible inconvenience to the home owner. His goal is to not only meet, but to exceed all expectations and requirements of our valued customers.</p>
  </div>
  <div class="sep"></div>
</div>

<div class="member" style="top:2236px">
  <div class="photo" role="img" aria-label="Portrait of Gerald Whitlock"></div>
  <div class="info">
    <h3>Gerald Whitlock</h3><h4>Accounting</h4>
    <p>After managing large hotels for decades, Gerald is now overseeing all the financial aspects of the company.</p>
    <p>Gerald is married with 6 children and 18 grandchildren.</p>
  </div>
  <div class="sep"></div>
</div>

<div class="member" style="top:2499px">
  <div class="photo" role="img" aria-label="Portrait of Marisa Delgado"></div>
  <div class="info">
    <h3>Marisa Delgado</h3><h4>Administrative Assistant</h4>
    <p>Marisa grew up around the construction industry, frequently working with her dad and others on various jobs. Her other work experience has been largely customer service related. She enjoys the opportunity to use both of these areas of experience in working for Quellmark.</p>
  </div>
  <div class="sep"></div>
</div>

<div class="member" style="top:2762px">
  <div class="photo" role="img" aria-label="Portrait of Colin Ashby"></div>
  <div class="info">
    <h3>Colin Ashby</h3><h4>Operations Manager (Interiors)</h4>
    <p>Colin manages a new division of Quellmark focusing on kitchens, bathrooms, and basement developments as well as other interior renovation needs.</p>
    <p>Colin is a talented guitar player and enjoys the outdoors, farming, fossils, and everything nature. He is married and a father of one with a new baby arriving around the end of 2017.</p>
  </div>
</div>

<div class="footer-band"></div>

<div class="abs panel-shadow2"></div>
<div class="abs panel-shadow1"></div>
<form class="abs panel">
  <h2 class="abs sec-title" style="left:0;width:877px;top:55px">QUICK <em>INQUIRY</em></h2>
  <div class="abs sec-bar" style="left:409px;top:96px"></div>
</form>
<div class="field" style="left:204px;top:3151px;width:383px;height:42px">Name*</div>
<div class="field" style="left:609px;top:3151px;width:383px;height:42px">Phone*</div>
<div class="field" style="left:204px;top:3206px;width:383px;height:42px">Email*</div>
<div class="field" style="left:609px;top:3206px;width:383px;height:42px">Choose a Service
  <svg class="abs" style="right:16px;top:17px" width="10" height="7" viewBox="0 0 10 7"><path d="M1 1l4 4 4-4" fill="none" stroke="#555" stroke-width="1.4"/></svg>
</div>
<div class="field" style="left:204px;top:3262px;width:788px;height:97px">Message*</div>
<div class="abs captcha"><i></i>I'm not a robot</div>
<div class="abs submit">SUBMIT</div>

<div class="abs chat">
  <svg width="34" height="34" viewBox="0 0 34 34" fill="none" stroke="#0d6fc0" stroke-width="2">
    <path d="M15 4a11 11 0 1 0 0 22h1l5 4v-6a11 11 0 0 0-6-20z"/>
    <path d="M12 12a3 3 0 1 1 4 3v2"/><circle cx="16" cy="20" r=".6" fill="#0d6fc0"/>
  </svg>
</div>

<div class="brand foot-brand"><span class="brand-dot"></span>QUELLMARK</div>
<nav class="foot-menu">
  <span style="left:288px">HOME</span><i style="left:360px"></i>
  <span style="left:387px">ABOUT US</span><i style="left:490px"></i>
  <span style="left:517px">SERVICES</span><i style="left:615px"></i>
  <span style="left:642px">MEET THE TEAM</span><i style="left:789px"></i>
  <span style="left:816px">CONTACT US</span>
</nav>

<div class="contact" style="left:97px">
  <svg width="30" height="46" viewBox="0 0 30 46" fill="none" stroke="#fff" stroke-width="2"><rect x="2" y="2" width="26" height="42" rx="4"/><path d="M2 9h26M2 36h26"/><circle cx="15" cy="40" r="1.5"/></svg>
  <b>PHONE</b><span>+1 780-555-0148</span>
</div>
<div class="contact" style="left:433px">
  <svg width="34" height="46" viewBox="0 0 34 46" fill="none" stroke="#fff" stroke-width="2"><path d="M17 44S3 27 3 17a14 14 0 0 1 28 0c0 10-14 27-14 27z"/><circle cx="17" cy="17" r="5"/></svg>
  <b>QUELLMARK EXTERIORS</b><span>48210 Range Rd 219 #117, Sherwood<br>Park, AB T8B 0X4, Canada</span>
</div>
<div class="contact" style="left:764px">
  <svg width="50" height="40" viewBox="0 0 50 40" fill="none" stroke="#fff" stroke-width="2"><rect x="2" y="4" width="46" height="32"/><path d="M2 4l23 18 23-18M2 36l17-16M48 36L31 20"/></svg>
  <b>EMAIL</b><span>info@quellmarkbuilders.ca</span>
</div>

<footer class="abs bottom">
  <p>Copyright © 2020 QUELLMARK EXTERIORS. All Rights Reserved.</p>
  <span class="social" style="left:889px"></span>
  <span class="social" style="left:929px"></span>
  <span class="social" style="left:969px"></span>
  <span class="social" style="left:1008px"></span>
</footer>

</body>
</html>
```